Website for Vetra Kolan Holdings

Need a project marketing website for our company which primarily deals in selling real estate(land sales) from Big Estates to Builders /Clients, help them in Building & Construction and do all Project Management.

Coding

Coded - Design and coding required

Number of Pages Required

4 page

Colors
0054AA
0677BA
7BADD7
CADEEF
E8F1F8
FFC000
F8CF3A
FAE287
FDF2CF
FEFAEE

```html
<!DOCTYPE html>
<html lang="en">
<head>
<meta charset="utf-8">
<title>Vetra Kolan Holdings</title>
<link rel="stylesheet" href="https://fonts.googleapis.com/css2?family=Poppins:wght@500;600;700&family=Montserrat:wght@400;500;600&display=swap">
<style>
:root{
  --navy:#0f2c3f;
  --accent:#1ba3dc;
  --text:#5a6570;
  --hero-dark:#2c3238;
  --soft:#eef4fa;
  --footer:#1e2830;
  --white:#ffffff;
  --line:#d6e2ee;
}
*{box-sizing:border-box;margin:0;padding:0}
html,body{width:1200px;height:4147px;overflow:hidden}
body{position:relative;background:var(--white);font-family:"Montserrat",sans-serif;color:var(--text)}
.abs{position:absolute}
h1,h2,h3,.brand{font-family:"Poppins",sans-serif;color:var(--navy)}
.brand{font-weight:700;font-size:20px;letter-spacing:.5px}
.site-header{left:0;top:0;width:1200px;height:84px}
.site-header .brand{left:66px;top:29px}
.nav{display:flex;gap:30px;right:238px;top:34px;font-size:15px;font-weight:500;color:var(--navy);list-style:none}
.btn{display:flex;align-items:center;justify-content:center;background:var(--accent);color:var(--white);font-family:"Poppins",sans-serif;font-weight:600;font-size:12px;letter-spacing:.4px;text-transform:uppercase}
.nav-cta{left:1016px;top:24px;width:118px;height:40px;text-transform:none;font-size:15px;font-weight:500;letter-spacing:0}
.hero{left:0;top:84px;width:1200px;height:572px}
.hero h1{left:66px;top:144px;width:640px;color:var(--white);font-size:37px;line-height:46px;font-weight:700;white-space:nowrap}
.hero p{left:66px;top:254px;width:600px;color:#d9dde1;font-size:15px;line-height:23px;white-space:nowrap}
.hero .btn{left:66px;top:351px;width:150px;height:39px}
.bar{width:36px;height:5px;background:var(--accent)}
.center{left:0;width:1200px;text-align:center}
.section-title{font-size:40px;line-height:46px;font-weight:700}
.lead{font-size:15px;line-height:23px}
.values{left:66px;top:1030px;width:1068px;display:flex;justify-content:space-between}
.value{width:330px;text-align:center}
.value svg{display:block;margin:0 auto}
.value h3{font-size:25px;font-weight:600;margin-top:24px}
.value p{font-size:13.5px;line-height:20px;margin-top:16px}
.services-head h2{font-size:40px;font-weight:700}
.outline-btn{left:1042px;top:1437px;width:92px;height:42px;border:1.5px solid var(--accent);color:var(--accent);font-size:14px;display:flex;align-items:center;justify-content:center}
.service{top:1545px;width:338px}
.photo{width:100%}
.service .photo{height:225px}
.service h3{font-size:20px;font-weight:600;margin-top:28px;white-space:nowrap}
.service p{font-size:13.5px;line-height:20px;margin-top:8px}
.service .more{display:flex;align-items:center;gap:14px;color:var(--accent);font-size:13px;margin-top:16px}
.project{overflow:hidden}
.project .photo{position:absolute;inset:0;height:100%}
.project .shade{position:absolute;left:0;right:0;bottom:0;height:55%;background:linear-gradient(to bottom,rgba(20,26,32,0),rgba(20,26,32,.85))}
.project .info{position:absolute;left:36px;bottom:36px;width:340px}
.project h3{color:var(--white);font-size:20px;font-weight:600;border-left:4px solid var(--accent);padding-left:10px;line-height:22px}
.project p{color:#cfd5da;font-size:13.5px;line-height:20px;margin-top:10px}
.contact{left:0;top:3219px;width:1200px;height:651px;background:var(--soft)}
.contact h2{left:66px;top:56px;font-size:40px;font-weight:700}
.contact .lead{left:66px;top:128px}
.contact-list{left:66px;top:182px;list-style:none;font-size:14px;color:var(--text)}
.contact-list li{display:flex;align-items:center;gap:16px;height:34px}
.contact-list a{color:var(--text)}
.form label{display:block;font-size:13.5px;color:var(--text)}
.field{background:var(--white);border:1px solid var(--line);width:500px}
.form .ph{font-size:13px;color:#9aa4ad;padding:14px 10px}
.check{display:flex;align-items:center;gap:8px;font-size:12.5px;color:var(--navy)}
.check span.box{width:17px;height:17px;border:1.5px solid #8a96a0;background:var(--white)}
.check a{color:var(--navy)}
.form .btn{width:132px;height:39px;font-size:14px;text-transform:none;font-weight:500}
.footer{left:0;top:3870px;width:1200px;height:277px;background:var(--footer)}
.footer .brand{color:var(--white);left:107px;top:76px}
.footer-nav{left:407px;top:84px;display:flex;gap:27px;list-style:none;font-family:"Poppins",sans-serif;color:var(--white);font-size:12.5px;font-weight:500}
.social{left:995px;top:82px;display:flex;gap:11px}
.social span{width:18px;height:18px;border-radius:50%;background:var(--white)}
.footer hr{position:absolute;left:66px;top:161px;width:1068px;border:0;border-top:1px solid #46525c}
.legal{left:0;top:190px;width:1200px;display:flex;justify-content:center;gap:20px;font-size:12px;color:#b9c1c8}
.legal a{color:#b9c1c8}
</style>
</head>
<body>

<header class="site-header abs">
  <div class="brand abs">Vetra Kolan Holdings</div>
  <ul class="nav abs"><li>Home</li><li>About Us</li><li>Our Services</li><li>Projects</li></ul>
  <div class="btn nav-cta abs">Contact Us</div>
</header>

<section class="hero abs">
  <svg class="abs" width="1200" height="572" viewBox="0 0 1200 572" role="img" aria-label="City street with modern glass skyscrapers against a blue sky">
    <defs>
      <linearGradient id="heroDark" x1="0" y1="0" x2="0" y2="1">
        <stop offset="0" stop-color="#2f353b"/><stop offset="1" stop-color="#3c434a"/>
      </linearGradient>
      <linearGradient id="heroSky" x1="0" y1="0" x2="0" y2="1">
        <stop offset="0" stop-color="#9fb6cf"/><stop offset=".45" stop-color="#3f5f88"/><stop offset="1" stop-color="#1a2a44"/>
      </linearGradient>
    </defs>
    <rect width="1200" height="572" fill="url(#heroDark)"/>
    <path d="M800 0 C700 190 600 390 540 572 L1200 572 L1200 0 Z" fill="url(#heroSky)"/>
    <path d="M781 0 C675 180 560 380 500 572 L542 572 C600 390 700 190 800 0 Z" fill="#1ba3dc"/>
  </svg>
  <h1 class="abs">Invest Smarter: Maximizing<br>Your Property Potential.</h1>
  <p class="abs">Lorem ipsum dolor sit amet, consectetur adipiscing elit.<br>Suspendisse varius enim in eros elementum tristique. Duis cursus,<br>mi quis viverra</p>
  <div class="btn abs">Raed More</div>
</section>

<div class="bar abs" style="left:582px;top:736px"></div>
<h2 class="section-title center abs" style="top:772px">Connecting You with Extraordinary<br>Properties</h2>
<p class="lead center abs" style="top:883px;padding:0 280px">Lorem ipsum dolor sit amet, consectetur adipiscing elit. Suspendisse varius enim in eros elementum tristique. Duis cursus, mi quis viverra ornare, eros dolor interdum nulla, ut commodo diam libero vitae erat.</p>

<div class="values abs">
  <div class="value">
    <svg width="50" height="50" viewBox="0 0 50 50" fill="none" stroke="#1ba3dc" stroke-width="2.6" stroke-linejoin="round"><path d="M10 4 L19 24 M40 4 L31 24 M10 4 H20 L25 15 L30 4 H40"/><circle cx="25" cy="33" r="12"/><path d="M25 27 l2 4 4 .5-3 3 .8 4.2-3.8-2-3.8 2 .8-4.2-3-3 4-.5z" stroke-width="1.6"/></svg>
    <h3>Experience</h3>
    <p>Lorem ipsum dolor sit amet, consectetur adipiscing elit. Suspendisse varius enim in eros elementum tristique. Duis cursus, mi quis viverra ornare, eros dolor interdum nulla.</p>
  </div>
  <div class="value">
    <svg width="50" height="50" viewBox="0 0 50 50" fill="none" stroke="#1ba3dc" stroke-width="2.6" stroke-linejoin="round"><path d="M21 4h8l1.5 5 4.5 2 4.5-2.5 5.5 5.5-2.5 4.5 2 4.5 5 1.5v8l-5 1.5-2 4.5 2.5 4.5-5.5 5.5-4.5-2.5-4.5 2-1.5 5h-8l-1.5-5-4.5-2-4.5 2.5-5.5-5.5 2.5-4.5-2-4.5-5-1.5v-8l5-1.5 2-4.5-2.5-4.5 5.5-5.5 4.5 2.5 4.5-2z" transform="scale(.9) translate(2.5 2.5)"/><path d="M25 16l8 3v6c0 5-4 8-8 9-4-1-8-4-8-9v-6z"/></svg>
    <h3>Integrity</h3>
    <p>Lorem ipsum dolor sit amet, consectetur adipiscing elit. Suspendisse varius enim in eros elementum tristique. Duis cursus, mi quis viverra ornare, eros dolor interdum nulla.</p>
  </div>
  <div class="value">
    <svg width="50" height="50" viewBox="0 0 50 50" fill="none" stroke="#1ba3dc" stroke-width="2.6" stroke-linejoin="round"><path d="M25 3l5 4 6-1 2 6 6 2-1 6 4 5-4 5 1 6-6 2-2 6-6-1-5 4-5-4-6 1-2-6-6-2 1-6-4-5 4-5-1-6 6-2 2-6 6 1z"/><path d="M17 25l6 6 11-12" stroke-linecap="round"/></svg>
    <h3>Results</h3>
    <p>Lorem ipsum dolor sit amet, consectetur adipiscing elit. Suspendisse varius enim in eros elementum tristique. Duis cursus, mi quis viverra ornare, eros dolor interdum nulla.</p>
  </div>
</div>

<div class="btn abs" style="left:525px;top:1313px;width:150px;height:39px">Raed More</div>

<div class="services-head">
  <h2 class="abs" style="left:66px;top:1388px">Our Services</h2>
  <p class="lead abs" style="left:66px;top:1456px">Lorem ipsum dolor sit amet, consectetur adipiscing elit.</p>
  <div class="outline-btn abs">View all</div>
</div>

<article class="service abs" style="left:66px">
  <div class="photo" role="img" aria-label="Modern white villa with a swimming pool" style="background:linear-gradient(to bottom,#8fb4d9 0%,#d9d4cc 55%,#4fa8a8 100%)"></div>
  <h3>Property Valuation</h3>
  <p>Lorem ipsum dolor sit amet, consectetur adipiscing elit. Suspendisse varius enim in eros.</p>
  <div class="more">View event <svg width="8" height="12" viewBox="0 0 8 12"><path d="M2 2l4 4-4 4" fill="none" stroke="#1ba3dc" stroke-width="1.8"/></svg></div>
</article>
<article class="service abs" style="left:431px">
  <div class="photo" role="img" aria-label="Hands passing a set of house keys across a desk" style="background:linear-gradient(to bottom,#cfd4d8,#eef0f1 60%,#d8c8bd)"></div>
  <h3>Transaction Management</h3>
  <p>Lorem ipsum dolor sit amet, consectetur adipiscing elit. Suspendisse varius enim in eros.</p>
  <div class="more">View event <svg width="8" height="12" viewBox="0 0 8 12"><path d="M2 2l4 4-4 4" fill="none" stroke="#1ba3dc" stroke-width="1.8"/></svg></div>
</article>
<article class="service abs" style="left:796px">
  <div class="photo" role="img" aria-label="Agent advising a couple inside a bright apartment" style="background:linear-gradient(to bottom,#d9dcde,#b9bec2 60%,#8a7f72)"></div>
  <h3>Consulting and Advisory</h3>
  <p>Lorem ipsum dolor sit amet, consectetur adipiscing elit. Suspendisse varius enim in eros.</p>
  <div class="more">View event <svg width="8" height="12" viewBox="0 0 8 12"><path d="M2 2l4 4-4 4" fill="none" stroke="#1ba3dc" stroke-width="1.8"/></svg></div>
</article>

<div class="bar abs" style="left:582px;top:1994px"></div>
<h2 class="section-title center abs" style="top:2026px">Recent Projects</h2>
<p class="lead center abs" style="top:2096px">Lorem ipsum dolor sit amet, consectetur adipiscing elit.</p>

<article class="project abs" style="left:66px;top:2185px;width:520px;height:533px">
  <div class="photo" role="img" aria-label="White colonial-style house with palm trees and a pool" style="background:linear-gradient(to bottom,#3d8ad0 0%,#b9cbd9 35%,#e2e2de 60%,#7d8a8a 100%)"></div>
  <div class="shade"></div>
  <div class="info"><h3>Project Name</h3><p>Lorem ipsum dolor sit amet, consectetur adipiscing elit. Suspendisse varius enim in eros.</p></div>
</article>
<article class="project abs" style="left:614px;top:2185px;width:519px;height:344px">
  <div class="photo" role="img" aria-label="Modern townhouses at dusk with lit windows" style="background:linear-gradient(120deg,#5b6a5e 0%,#7b8a86 45%,#8f8aa8 75%,#d3a779 100%)"></div>
  <div class="shade"></div>
  <div class="info"><h3>Project Name</h3><p>Lorem ipsum dolor sit amet, consectetur adipiscing elit. Suspendisse varius enim in eros.</p></div>
</article>
<article class="project abs" style="left:614px;top:2558px;width:519px;height:532px">
  <div class="photo" role="img" aria-label="Twin high-rise towers under construction with cranes" style="background:linear-gradient(to bottom,#2f9ad6 0%,#8ec3df 45%,#9a9686 75%,#5c5b52 100%)"></div>
  <div class="shade"></div>
  <div class="info"><h3>Project Name</h3><p>Lorem ipsum dolor sit amet, consectetur adipiscing elit. Suspendisse varius enim in eros.</p></div>
</article>
<article class="project abs" style="left:66px;top:2745px;width:520px;height:345px">
  <div class="photo" role="img" aria-label="Glass office towers seen from below against clouds" style="background:linear-gradient(110deg,#6d93bf 0%,#c7d5e3 35%,#3c5a80 70%,#223a5c 100%)"></div>
  <div class="shade"></div>
  <div class="info"><h3>Project Name</h3><p>Lorem ipsum dolor sit amet, consectetur adipiscing elit. Suspendisse varius enim in eros.</p></div>
</article>

<div class="btn abs" style="left:525px;top:3140px;width:150px;height:39px">View More</div>

<section class="contact abs">
  <h2 class="abs">Contact us</h2>
  <p class="lead abs">Lorem ipsum dolor sit amet, consectetur adipiscing elit.</p>
  <ul class="contact-list abs">
    <li><svg width="18" height="14" viewBox="0 0 18 14" fill="none" stroke="#1ba3dc" stroke-width="1.6"><rect x="1" y="1" width="16" height="12" rx="1"/><path d="M1 2l8 6 8-6"/></svg><a href="#">email@example.com</a></li>
    <li><svg width="18" height="18" viewBox="0 0 18 18" fill="none" stroke="#1ba3dc" stroke-width="1.6"><path d="M4 1.5l3 3.5-2 2c1 2.5 3 4.5 5.5 5.5l2-2 3.5 3-1.5 2.5C9 16 2 9 1.5 3z"/></svg><a href="#">+1 (555) 000-0000</a></li>
    <li><svg width="18" height="18" viewBox="0 0 18 18" fill="none" stroke="#1ba3dc" stroke-width="1.6"><path d="M9 17s6-6 6-10A6 6 0 0 0 3 7c0 4 6 10 6 10z"/><circle cx="9" cy="7" r="2.2"/></svg>123 Sample St, Sydney NSW 2000 AU</li>
  </ul>
  <form class="form">
    <label class="abs" style="left:633px;top:62px">Name</label>
    <div class="field abs" style="left:633px;top:87px;height:38px"></div>
    <label class="abs" style="left:633px;top:149px">Email</label>
    <div class="field abs" style="left:633px;top:174px;height:38px"></div>
    <label class="abs" style="left:633px;top:236px">Message</label>
    <div class="field abs" style="left:633px;top:261px;height:148px"><div class="ph">Type your message...</div></div>
    <div class="check abs" style="left:633px;top:429px"><span class="box"></span>I accept the <a href="#">Terms</a></div>
    <div class="btn abs" style="left:633px;top:481px">Submit</div>
  </form>
</section>

<footer class="footer abs">
  <div class="brand abs">Vetra Kolan Holdings</div>
  <ul class="footer-nav abs"><li>Home</li><li>About Us</li><li>Our Services</li><li>Projects</li><li>Contact Us</li></ul>
  <div class="social abs" aria-label="Social links"><span></span><span></span><span></span><span></span><span></span></div>
  <hr>
  <div class="legal abs"><span>© 2024 . All rights reserved.</span><a href="#">Privacy Policy</a><a href="#">Terms of Service</a><a href="#">Cookies Settings</a></div>
</footer>

</body>
</html>
```